Marrowind Lake Billboard

Looking to design a multi purpose billboard promoting Marrowind Lake as a destination point. Billboard size is 12ft x 40ft
My goal is to advertise our restaurant The Driftmill (pic attached)
What makes Marrowind a destination? It offers lodging / water skiing / Off Road Adventure / Camping / Fishing / Hunting
Want a catch phrase, something like "Looking For a Getaway" or "Need a Break"
Needs to really pop and catch the interest of the looker
maybe have our website address www.marrowinddriftmill.example
Open for ideas

```html
<!DOCTYPE html>
<html lang="en">
<head>
<meta charset="utf-8">
<title>The Driftmill – Marrowind Lake Billboard</title>
<link href="https://fonts.googleapis.com/css2?family=Alfa+Slab+One&family=Rye&family=Arvo:wght@700&family=Open+Sans:wght@700;800&display=swap" rel="stylesheet">
<style>
  :root {
    --page-bg: #ffffff;
    --wood-dark: #1f120b;
    --wood-mid: #3a2214;
    --wood-light: #4e2e1a;
    --accent-orange: #f28a1e;
    --ink-white: #ffffff;
    --ink-dark: #1a1a1a;
  }
  html, body {
    margin: 0;
    padding: 0;
    width: 1200px;
    height: 1200px;
    overflow: hidden;
    background: var(--page-bg);
  }
  .billboard {
    position: absolute;
    left: 40px;
    top: 432px;
    width: 1120px;
    height: 336px;
    display: block;
  }
  .headline {
    font-family: "Alfa Slab One", Georgia, serif;
    font-size: 60px;
    fill: var(--ink-white);
    stroke: var(--accent-orange);
    stroke-width: 7px;
    paint-order: stroke fill;
    stroke-linejoin: round;
    text-anchor: middle;
  }
  .headline-edge {
    font-family: "Alfa Slab One", Georgia, serif;
    font-size: 60px;
    fill: none;
    stroke: var(--ink-dark);
    stroke-width: 13px;
    stroke-linejoin: round;
    text-anchor: middle;
  }
  .brand-the, .brand-name {
    font-family: "Rye", Georgia, serif;
    fill: var(--ink-white);
    text-anchor: middle;
  }
  .brand-the { font-size: 30px; }
  .brand-name { font-size: 58px; }
  .brand-place {
    font-family: "Rye", Georgia, serif;
    font-size: 19px;
    fill: var(--ink-white);
    text-anchor: middle;
  }
  .web-address {
    font-family: "Arvo", Georgia, serif;
    font-weight: 700;
    font-size: 12px;
    fill: var(--ink-dark);
    text-anchor: middle;
  }
  .phone {
    font-family: "Open Sans", Arial, sans-serif;
    font-weight: 800;
    font-size: 44px;
    fill: var(--ink-white);
    text-anchor: middle;
    letter-spacing: -1px;
  }
  .food-frame { stroke: var(--accent-orange); stroke-width: 3; }
</style>
</head>
<body>
<svg class="billboard" viewBox="0 0 1120 336" xmlns="http://www.w3.org/2000/svg">
  <defs>
    <linearGradient id="wood" x1="0" y1="0" x2="1" y2="1">
      <stop offset="0" stop-color="var(--wood-light)"/>
      <stop offset="0.5" stop-color="var(--wood-mid)"/>
      <stop offset="1" stop-color="var(--wood-dark)"/>
    </linearGradient>
    <radialGradient id="storefront" cx="0.45" cy="0.7" r="0.8">
      <stop offset="0" stop-color="#8a5a2b"/>
      <stop offset="0.45" stop-color="#4a3524"/>
      <stop offset="1" stop-color="#1c2018"/>
    </radialGradient>
    <radialGradient id="food-wrap" cx="0.5" cy="0.5" r="0.6">
      <stop offset="0" stop-color="#c96a3a"/>
      <stop offset="0.55" stop-color="#7f8a3a"/>
      <stop offset="1" stop-color="#d9c3a0"/>
    </radialGradient>
    <radialGradient id="food-ribs" cx="0.5" cy="0.5" r="0.6">
      <stop offset="0" stop-color="#c8662e"/>
      <stop offset="1" stop-color="#5a2a14"/>
    </radialGradient>
  </defs>

  <rect class="wood-panel" x="0" y="0" width="1120" height="336" fill="url(#wood)"/>
  <rect class="storefront-photo" x="0" y="0" width="580" height="336" fill="url(#storefront)"
        role="img" aria-label="Photo of the rustic wooden restaurant storefront lit at dusk"/>

  <circle class="food-frame" cx="584" cy="294" r="55" fill="url(#food-ribs)"
          role="img" aria-label="Photo of grilled smoked ribs"/>
  <circle class="food-frame" cx="613" cy="52" r="52" fill="url(#food-ribs)"
          role="img" aria-label="Photo of grilled smoked ribs"/>
  <circle class="food-frame" cx="599" cy="181" r="92" fill="url(#food-wrap)"
          role="img" aria-label="Photo of a flatbread wrap with lettuce, tomato and sauce"/>

  <g class="catch-phrase">
    <text class="headline-edge" x="243" y="138">LOOKING</text>
    <text class="headline-edge" x="243" y="199">FOR A</text>
    <text class="headline-edge" x="243" y="262">GETAWAY</text>
    <text class="headline" x="243" y="138">LOOKING</text>
    <text class="headline" x="243" y="199">FOR A</text>
    <text class="headline" x="243" y="262">GETAWAY</text>
  </g>

  <g class="brand-block">
    <text class="brand-the" x="893" y="67">THE</text>
    <text class="brand-name" x="893" y="138" textLength="330" lengthAdjust="spacingAndGlyphs">DRIFTMILL</text>
    <text class="brand-place" x="893" y="178">MARROWIND LAKE &amp; DAM</text>
  </g>

  <g class="contact-block">
    <rect x="712" y="227" width="347" height="64" rx="10" fill="none" stroke="var(--accent-orange)" stroke-width="1.5"/>
    <rect x="768" y="213" width="236" height="26" rx="7" fill="var(--accent-orange)"/>
    <text class="web-address" x="886" y="230">www.marrowinddriftmill.example</text>
    <text class="phone" x="885" y="279">555-014-2277</text>
  </g>
</svg>
</body>
</html>
```